INNOVATIVE DESIGN NEEDED FOR FINANCIAL COMPANY

INTERNATIONAL FIRM IN HONG KONG NEEDS A MODERN BUSINESS CARD DESIGN. ONE SIDE ENGLISH OTHER SIDE IN CHINESE. WE ARE OPEN TO CHANGING FONTS AND COLOR. SHOULD BE A CARD THAT IS PROFESSIONAL DEALING WITH HIGH NET WORTH CLIENTELE. BOTH SIDES OF THE CARD WILL BE THE SAME, HOWEVER, THE WORDING ON ONE SIDE WILL BE ENGLISH AND THE OTHER SIDE IN CHINESE (CAN ASSIST IN THE LETTERING - CAN PROVIDE ONCE CARD DESIGN IS ACCEPTED.

Target Market(s)

Hong Kong/CHINA

Contact Information for Business Card

ATTRACTIVE MODERN

```html
<!DOCTYPE html>
<html lang="en">
<head>
<meta charset="utf-8">
<title>Larchway Asset Management – Business Cards</title>
<link rel="stylesheet" href="https://fonts.googleapis.com/css2?family=Open+Sans:wght@400;600;700&family=Noto+Sans+TC:wght@400;700&display=swap">
<style>
  :root{
    --bg:#e4e6e5;
    --green-deep:#06473a;
    --green-brand:#149a68;
    --paper:#f4f5f4;
    --ink:#2b2f2e;
    --ink-light:#f1f5f3;
    --rule-dark:#d9e6e0;
    --rule-light:#4d5150;
  }
  *{box-sizing:border-box;margin:0;padding:0}
  html,body{width:1200px;height:1021px;overflow:hidden}
  body{background:var(--bg);font-family:"Open Sans",sans-serif;position:relative}
  .card{
    position:absolute;width:660px;height:377px;
    box-shadow:0 14px 30px rgba(0,0,0,.22);
    display:flex;align-items:center;
  }
  .card--chinese{left:470px;top:100px;background:var(--green-deep);color:var(--ink-light)}
  .card--english{left:70px;top:540px;background:var(--paper);color:var(--ink)}
  .brand{
    width:370px;padding-left:46px;display:flex;align-items:center;gap:12px;
  }
  .brand__dot{width:36px;height:36px;border-radius:50%;background:var(--green-brand);flex:none}
  .brand__name{font-family:"Noto Sans TC",sans-serif;font-weight:700;line-height:1.25}
  .brand__zh{font-size:22px;letter-spacing:1px;display:block}
  .brand__en{font-size:10.5px;letter-spacing:.6px;display:block}
  .card--chinese .brand__name{color:#ffffff}
  .card--english .brand__name{color:#3a3d3c}
  .divider{width:2px;height:180px;flex:none}
  .card--chinese .divider{background:var(--rule-dark)}
  .card--english .divider{background:var(--rule-light)}
  .details{padding-left:30px;font-size:17px;line-height:1.32}
  .details__name{color:var(--green-brand);font-weight:700;font-size:24px;line-height:1.1}
  .card--chinese .details__name{font-family:"Noto Sans TC",sans-serif;font-weight:400;letter-spacing:4px}
  .details__title{font-size:17px;margin-bottom:18px}
  .card--chinese .details__title,.card--chinese .details__address{font-family:"Noto Sans TC","Open Sans",sans-serif}
  .details__address{margin-bottom:4px}
  .contact{display:flex;align-items:center;gap:8px}
  .contact svg{width:14px;height:14px;flex:none}
</style>
</head>
<body>

<section class="card card--chinese" aria-label="Chinese side">
  <div class="brand">
    <span class="brand__dot"></span>
    <span class="brand__name"><span class="brand__zh">恒林資產管理有限公司</span><span class="brand__en">Larchway Asset Management Ltd</span></span>
  </div>
  <div class="divider"></div>
  <div class="details">
    <p class="details__name">李文博</p>
    <p class="details__title">常務董事</p>
    <p class="details__address">1088 号松林路<br>上海, 中国 200120</p>
    <p class="contact"><svg viewBox="0 0 16 16"><path fill="#149a68" d="M3 1l3 3-1.5 2a9 9 0 005.5 5.5L12 10l3 3-2 2C7 15 1 9 1 3z"/></svg>(555) 210-4478</p>
    <p class="contact"><svg viewBox="0 0 16 16"><rect x="1" y="3" width="14" height="10" fill="none" stroke="#149a68" stroke-width="1.5"/><path d="M1 3l7 6 7-6" fill="none" stroke="#149a68" stroke-width="1.5"/></svg>daniel@larchwayasset.com</p>
    <p class="contact"><svg viewBox="0 0 16 16"><circle cx="8" cy="8" r="6.5" fill="none" stroke="#149a68" stroke-width="1.4"/><path d="M1.5 8h13M8 1.5c-3 3-3 10 0 13M8 1.5c3 3 3 10 0 13" fill="none" stroke="#149a68" stroke-width="1.2"/></svg>www.larchwayasset.com</p>
  </div>
</section>

<section class="card card--english" aria-label="English side">
  <div class="brand">
    <span class="brand__dot"></span>
    <span class="brand__name"><span class="brand__zh">恒林資產管理有限公司</span><span class="brand__en">Larchway Asset Management Ltd</span></span>
  </div>
  <div class="divider"></div>
  <div class="details">
    <p class="details__name">Daniel Hart</p>
    <p class="details__title">Managing Director</p>
    <p class="details__address">418 N. W. 5th Street<br>Coral Bay, Florida, 33140</p>
    <p class="contact"><svg viewBox="0 0 16 16"><path fill="#149a68" d="M3 1l3 3-1.5 2a9 9 0 005.5 5.5L12 10l3 3-2 2C7 15 1 9 1 3z"/></svg>(555) 210-4478</p>
    <p class="contact"><svg viewBox="0 0 16 16"><rect x="1" y="3" width="14" height="10" fill="none" stroke="#149a68" stroke-width="1.5"/><path d="M1 3l7 6 7-6" fill="none" stroke="#149a68" stroke-width="1.5"/></svg>daniel@larchwayasset.com</p>
    <p class="contact"><svg viewBox="0 0 16 16"><circle cx="8" cy="8" r="6.5" fill="none" stroke="#149a68" stroke-width="1.4"/><path d="M1.5 8h13M8 1.5c-3 3-3 10 0 13M8 1.5c3 3 3 10 0 13" fill="none" stroke="#149a68" stroke-width="1.2"/></svg>www.larchwayasset.com</p>
  </div>
</section>

</body>
</html>
```